Chartered accountants trying to make boring information more appealing!

We are UK based chartered accountants with various specialist areas of expertise. We need a template for a monthly mailer that we send to our clients and contacts to keep them updated with key financial news. The update is called Amber Reef and we'd like it to fit on one page of A4 that we can then drop text into. We would like it to be more appealing than just the usual calculators and audit papers associated with accountants. Our brand colours are blue and green.

Target Market(s)

Our clients range from small businesses to large pension fund trustees, charities and individuals. It must appeal to everyone.

Industry/Entity Type

Accounting

Colors
34a7d8
33b8a4
3277b5

Requirements
Must have
• Space for text. The title 'Amber Reef'. Our logo.
Nice to have
• Sky's the limit!
Should not have
• Shouldn't look homemade. I've attached an old one done in house - please avoid this!

```html
<!DOCTYPE html>
<html lang="en">
<head>
<meta charset="utf-8">
<title>Amber Reef – Accounting News</title>
<link href="https://fonts.googleapis.com/css2?family=Oswald:wght@500;600&family=Lato:ital,wght@0,400;0,700;0,900;1,700&family=Archivo+Black&display=swap" rel="stylesheet">
<style>
  :root {
    --sky: #34a7d8;
    --teal: #33b8a4;
    --blue: #3277b5;
    --navy: #1f5f9e;
    --green: #3a9a6a;
    --ink: #222;
    --body: #4a4a4a;
    --paper: #ffffff;
  }
  * { box-sizing: border-box; margin: 0; padding: 0; }
  html, body { width: 900px; height: 1200px; overflow: hidden; background: var(--paper); }
  .mailer { position: relative; width: 900px; height: 1200px; overflow: hidden; background: var(--paper); font-family: "Lato", sans-serif; color: var(--body); }
  .office-photo { position: absolute; left: 280px; top: 0; width: 420px; height: 380px;
    background: radial-gradient(ellipse at 60% 35%, #dfe3e8 0%, #eef0f3 45%, rgba(255,255,255,0) 75%); }
  .feature-art { position: absolute; left: 0; top: 0; width: 900px; height: 800px; }
  .brand { position: absolute; left: 62px; top: 44px; text-align: center; width: 260px; }
  .brand-name { font-family: "Lato", sans-serif; font-weight: 400; font-size: 56px; color: var(--navy); line-height: 1; }
  .brand-tag { font-size: 11px; letter-spacing: 2px; color: var(--navy); margin-top: 4px; }
  .headline { position: absolute; left: 36px; top: 182px; }
  .headline .kicker { font-family: "Oswald", sans-serif; font-weight: 500; font-size: 40px; color: var(--green); line-height: 1.1; }
  .headline .lead { font-family: "Lato", sans-serif; font-weight: 700; font-size: 44px; color: var(--blue); line-height: 1.1; }
  .headline .big { font-family: "Archivo Black", sans-serif; font-size: 53px; color: var(--ink); line-height: 1.12; }
  .intro { position: absolute; left: 38px; top: 423px; width: 590px; font-weight: 900; font-size: 13px; color: var(--ink); line-height: 1.3; }
  .section-title { position: absolute; left: 38px; font-weight: 700; font-size: 19px; color: var(--blue); }
  .copy { position: absolute; left: 38px; width: 700px; font-weight: 700; font-size: 12.5px; line-height: 1.3; color: var(--body); }
  .copy p + p { margin-top: 12px; }
  .copy .price { color: var(--sky); }
  .banner { position: absolute; left: 0; height: 36px; padding-left: 42px; display: flex; align-items: center;
    background: linear-gradient(90deg, var(--blue), var(--sky)); border-radius: 0 14px 14px 0;
    font-family: "Oswald", sans-serif; font-weight: 500; font-size: 20px; color: #fff; }
  .checklist { position: absolute; left: 40px; top: 664px; list-style: none; }
  .checklist li { position: relative; padding-left: 26px; font-weight: 700; font-size: 16px; color: #3d3d3d; line-height: 1.3; }
  .checklist li::before { content: ""; position: absolute; left: 2px; top: 6px; width: 11px; height: 11px; border-radius: 50%; background: var(--teal); }
  .subhead { position: absolute; left: 38px; top: 896px; font-style: italic; font-weight: 700; font-size: 19px; color: var(--teal); }
  .web-link { display: block; font-size: 17px; color: var(--navy); margin-top: 3px; }
  .strong-ink { color: var(--ink); }
  .edge-tab { position: absolute; right: 0; width: 76px; height: 32px; background: linear-gradient(90deg, var(--blue), var(--sky)); }
  .edge-line { position: absolute; height: 2px; width: 40px; background: var(--sky); }
  .footer-band { position: absolute; left: 0; top: 1120px; width: 620px; height: 80px;
    background: linear-gradient(90deg, var(--blue), var(--sky));
    clip-path: polygon(0 0, 96% 0, 100% 100%, 0 100%); }
  .footer-note { position: absolute; left: 44px; top: 1130px; width: 420px;
    font-style: italic; font-weight: 700; font-size: 13px; line-height: 1.3; color: #fff; }
  .footer-next { position: absolute; left: 600px; top: 1142px; width: 300px; height: 58px; background: var(--teal);
    display: flex; align-items: center; justify-content: center; font-style: italic; font-weight: 700; font-size: 19px; color: #fff; }
</style>
</head>
<body>
<main class="mailer">
  <div class="office-photo" role="img" aria-label="Faint photo of business people meeting by an office window"></div>

  <svg class="feature-art" viewBox="0 0 900 800">
    <defs>
      <linearGradient id="deskTones" x1="0" y1="0" x2="1" y2="1">
        <stop offset="0" stop-color="#cfdbe6"/>
        <stop offset="0.5" stop-color="#8fa8c0"/>
        <stop offset="1" stop-color="#3c4a5a"/>
      </linearGradient>
    </defs>
    <polygon points="700,0 900,0 900,760 460,300" fill="var(--teal)"/>
    <polygon points="705,40 965,300 705,560 445,300" fill="#ffffff"/>
    <polygon points="705,58 947,300 705,542 463,300" fill="var(--sky)"/>
    <polygon points="705,66 939,300 705,534 471,300" fill="url(#deskTones)" role="img" aria-label="Photo of a laptop, calculator and paperwork on a desk"/>
  </svg>

  <div class="brand">
    <div class="brand-name">Harwell</div>
    <div class="brand-tag">CHARTERED ACCOUNTANTS</div>
  </div>

  <h1 class="headline">
    <div class="kicker">KEEPING YOU UP TO DATE</div>
    <div class="lead">with the latest</div>
    <div class="big">ACCOUNTING<br>NEWS</div>
  </h1>

  <p class="intro">Welcome to Harwell Amber Reef. This issue covers the new National Living Wage, PAYE Settlement Agreements and the latest news on pension contributions due to be announced in the Budget</p>

  <h2 class="section-title" style="top:482px">The new National Living Wage (“NLW”)</h2>
  <div class="copy" style="top:514px;width:650px">
    <p>From April 2016, the Government’s new National Living Wage will become law. This means that all workers aged 25 and over are legally entitled to be paid at least <span class="price">£7.20</span> per hour.</p>
    <p>If you’re an employer, you will need to make sure that you are paying your staff correctly from 1st April, as the National Living Wage will be enforced just as strongly as the current National Minimum Wage.</p>
  </div>

  <div class="banner" style="top:612px;width:600px">To make sure that you are ready for the change, you must:</div>
  <ul class="checklist">
    <li>Check which of your employees is eligible to receive the NLW</li>
    <li>Take the appropriate payroll actions</li>
    <li>Let your staff know about their new pay rates</li>
    <li>Check that your staff under 25 are earning at least the right rate of National Minimum Wage</li>
  </ul>
  <div class="copy" style="top:756px">
    <p>If you’re concerned about the effects of the new National Living Wage or would like some help to implement the changes, why not call one of our Payroll experts on 0123 456 7890 for some specialist advice?</p>
  </div>

  <div class="banner" style="top:804px;width:606px">PAYE Settlement Agreements (“PSA”)</div>
  <div class="copy" style="top:848px">
    <p>A PSA allows an employer to make one annual payment to cover all the tax and National Insurance due on small or irregular taxable benefits or expenses. This can be beneficial as it avoids the need to include these on annual P11D forms, or to calculate and charge tax and National Insurance on such items through the payroll.</p>
  </div>
  <h3 class="subhead">What is covered?</h3>
  <div class="copy" style="top:926px">
    <p>A PSA is intended to cover items that are minor irregular gifts, such as a small birthday present, gift voucher, staff entertaining or one off relocation expenses. It can also include items where it would be impracticable to either operate PAYE on the amount, or difficult to identify with a shared benefit, how much relates to each employee in order to report it on a form P11D, e.g. the cost of a staff Christmas party, that doesn’t qualify for relief.</p>
    <p>A PSA cannot be used for items such as bonuses, round sum allowances, beneficial loans or more high-value benefits such as company cars.</p>
    <p>If you apply after the start of the tax year, there are some restrictions on what you can include.<br>
      <span class="strong-ink">You can find out more about the National Living Wage, including new rates of pay on the Government website at</span>
      <span class="web-link">www.example.org/living-wage</span></p>
  </div>

  <div class="edge-line" style="left:784px;top:778px"></div>
  <div class="edge-line" style="left:784px;top:784px"></div>
  <div class="edge-tab" style="top:764px"></div>
  <div class="edge-line" style="left:784px;top:888px"></div>
  <div class="edge-line" style="left:784px;top:894px"></div>
  <div class="edge-tab" style="top:874px"></div>
  <div class="edge-line" style="left:784px;top:996px"></div>
  <div class="edge-line" style="left:784px;top:1002px"></div>
  <div class="edge-tab" style="top:982px"></div>

  <div class="footer-next">Continued overleaf…</div>
  <div class="footer-band"></div>
  <p class="footer-note">This paper is intended as a guide and does not deal with any issue in great depth. For tailored individual advice or further information please contact our team to find out how this could affect you.</p>
</main>
</body>
</html>
```